Software Specialist in Artificial Intelligence innovation needs a smart and professional looking bus

Prefers a clean and professional design, yet portraying a class of its own and a world-class feel. We develop state-of-the-art software automation engines by deploying artificial intelligence that simulates the smartest brains that are able to simulate a human consultant and/or data scientist. Both single-sided or double-sided design is acceptable. Do not refer too much to our current website as we are also in the process of revamping it so that it better reflects who we are and what we do.
Updates

Project Deadline Extended
Reason: A substantial number of designs submitted to date deviates a fair bit from requirements and expectations. Feedbacks will be provided to all parties by today and as such, an extension is catered to accomodate re-submissions.

Target Market(s)

Software technology companies, software developers, enterprise clients that requires automation supported by Artificial Intelligence driven software solutions.

Industry/Entity Type

Software

Contact Information for Business Card

Marcus Tan
Chief Innovator
marcustan@veltrixia.com
mobile: +65 94567312
Company Name: Veltrixia Pte Ltd
Address: 14 Sorbank Road #05-11 Harlowe Point, Singapore 538422
Telephone: +65 63417250
Website: www.Veltrixia.com
Please do not include the titles of the above fields.

Font styles to use
Sans Serif
Other font styles liked:
• Calibri, Futura Condensed

Requirements
Must have
• Portrays a professional and innovative image. Should reflect that the company is into Artificial Intelligence software development, high tech kind of feel.
Nice to have
• A plus point would be if you can even come up with a new company logo for us, representing who we are. Our current company logo is attached.
Should not have
• Fanciful stuffs as it must portray a professional image. Prefers not to have the cloud "image" as part of the logo or in the name card.

```html
<!DOCTYPE html>
<html lang="en">
<head>
<meta charset="utf-8">
<title>Veltrixia – Marcus Tan Business Card</title>
<link rel="stylesheet" href="https://fonts.googleapis.com/css2?family=PT+Sans+Narrow:wght@400;700&family=Open+Sans:wght@600;700&family=Questrial&display=swap">
<style>
  :root {
    --brand-red: #d80c2b;
    --ink-dark: #1e1e1e;
    --white: #ffffff;
    --grey-mid: #8a8a8a;
    --grey-light: #f4f4f4;
    --black: #000000;
    --charcoal: #4b4b4b;
  }
  * { margin: 0; padding: 0; box-sizing: border-box; }
  html, body {
    width: 1200px;
    height: 702px;
    overflow: hidden;
    background: var(--white);
  }
  .business-card {
    position: absolute;
    left: 59px;
    top: 86px;
    width: 1085px;
    height: 559px;
    background: linear-gradient(to bottom,
      var(--white) 0px,
      var(--white) 112px,
      var(--grey-light) 150px,
      var(--grey-mid) 372px);
    overflow: hidden;
  }
  .name-tab {
    position: absolute;
    left: 0;
    top: 0;
    width: 464px;
    height: 116px;
    background: var(--brand-red);
    border-radius: 0 46px 18px 0;
    box-shadow: 4px 5px 5px rgba(0,0,0,0.45);
  }
  .person-name {
    position: absolute;
    left: 68px;
    top: 6px;
    font-family: "PT Sans Narrow", sans-serif;
    font-weight: 700;
    font-size: 52px;
    line-height: 1.1;
    color: var(--white);
    letter-spacing: 0.5px;
  }
  .person-title {
    position: absolute;
    left: 74px;
    top: 62px;
    font-family: "PT Sans Narrow", sans-serif;
    font-weight: 400;
    font-size: 28px;
    color: var(--white);
  }
  .brand {
    position: absolute;
    left: 600px;
    top: 2px;
    width: 460px;
    text-align: center;
  }
  .brand-name {
    display: inline-flex;
    align-items: center;
    gap: 14px;
    font-family: "Open Sans", sans-serif;
    font-weight: 700;
    font-size: 66px;
    line-height: 1.1;
    color: var(--brand-red);
    letter-spacing: -1px;
  }
  .brand-dot {
    width: 32px;
    height: 32px;
    border-radius: 50%;
    background: var(--brand-red);
  }
  .brand-tagline {
    margin-top: 2px;
    font-family: "Open Sans", sans-serif;
    font-weight: 600;
    font-size: 24px;
    color: var(--ink-dark);
    letter-spacing: -0.2px;
    white-space: nowrap;
  }
  .address {
    position: absolute;
    left: 40px;
    top: 240px;
    width: 580px;
    text-align: center;
    font-family: "Questrial", sans-serif;
    font-style: normal;
    font-size: 27px;
    line-height: 1.4;
    letter-spacing: 0.6px;
    color: var(--brand-red);
  }
  .accent-band {
    position: absolute;
    left: 0;
    top: 371px;
    width: 100%;
    height: 53px;
    background: var(--brand-red);
    box-shadow: 0 4px 6px rgba(0,0,0,0.6);
    z-index: 2;
  }
  .contact-bar {
    position: absolute;
    left: 0;
    top: 424px;
    width: 100%;
    height: 135px;
    background: linear-gradient(to bottom, var(--charcoal), var(--black));
  }
  .contact-item {
    position: absolute;
    display: flex;
    align-items: center;
    font-family: "PT Sans Narrow", sans-serif;
    font-size: 27px;
    color: var(--white);
  }
  .contact-item svg { flex: none; }
  .mobile, .landline { gap: 24px; }
  .email, .website { gap: 24px; font-size: 29px; letter-spacing: 0.4px; }
  .mobile { left: 68px; top: 14px; }
  .landline { left: 67px; top: 57px; }
  .email { left: 725px; top: 14px; }
  .website { left: 722px; top: 53px; }
</style>
</head>
<body>
  <main class="business-card">
    <header class="name-tab">
      <h1 class="person-name">Marcus Tan</h1>
      <p class="person-title">Chief Innovator</p>
    </header>

    <div class="brand">
      <div class="brand-name"><span class="brand-dot"></span>Veltrixia</div>
      <p class="brand-tagline">Engineering the Intelligent Enterprise</p>
    </div>

    <address class="address">
      14 Sorbank Road #05-11 Harlowe Point,<br>Singapore 538422
    </address>

    <div class="accent-band"></div>

    <section class="contact-bar">
      <div class="contact-item mobile">
        <svg width="26" height="26" viewBox="0 0 26 26" aria-hidden="true">
          <rect x="1" y="1" width="24" height="24" rx="5" fill="#fff"/>
          <path d="M9 5c-1.5.3-3 1.6-2.6 4 .6 4 3.7 8.6 7.6 11 2 1.1 3.6.6 4.6-.7l-3-3c-.8.4-1.5.7-2.3 0-1.3-1.2-2.6-3-3-4.4-.3-1 .3-1.5 1-1.9L9 5z" fill="#111"/>
        </svg>
        <span>+65 94567312</span>
      </div>
      <div class="contact-item landline">
        <svg width="28" height="24" viewBox="0 0 28 24" aria-hidden="true">
          <path d="M2 8c0-3 5-5 12-5s12 2 12 5v2h-6V7.5c-2-.6-10-.6-12 0V10H2z" fill="#fff"/>
          <path d="M7 11h14l3 11H4z" fill="#fff"/>
          <circle cx="14" cy="16" r="3" fill="#111"/>
        </svg>
        <span>+65 63417250</span>
      </div>
      <div class="contact-item email">
        <svg width="34" height="22" viewBox="0 0 34 22" aria-hidden="true">
          <rect x="1" y="2" width="32" height="18" fill="#fff"/>
          <path d="M1 2l16 11L33 2" fill="none" stroke="#222" stroke-width="1.6"/>
          <path d="M1 20l12-9M33 20l-12-9" fill="none" stroke="#222" stroke-width="1.2"/>
        </svg>
        <span>marcustan@veltrixia.com</span>
      </div>
      <div class="contact-item website">
        <svg width="40" height="26" viewBox="0 0 40 26" aria-hidden="true">
          <g fill="none" stroke="#fff" stroke-width="1.6">
            <circle cx="12" cy="12" r="10"/>
            <ellipse cx="12" cy="12" rx="4.5" ry="10"/>
            <path d="M2 12h20M4 6.5h16M4 17.5h16"/>
            <circle cx="26" cy="14" r="5"/>
          </g>
          <path d="M30 18l8 6" stroke="#fff" stroke-width="3.5" stroke-linecap="round"/>
        </svg>
        <span>www.Veltrixia.com</span>
      </div>
    </section>
  </main>
</body>
</html>
```